Beyond the Hunt Product Labeling

We need a label design for a new product we are launching. We have developed a cooking bag that will cook your fish or game bird instantly. This is for the everyday fisherman and upland game hunter. This label will be printed on a thin sticker on the front of a Mylar Bag. The Mylar Bag is 9 1/2 x 12 inches. Inside the Mylar Bag is 3 cooking bags.
Target Market(s)
hunters and fishermen
Industry/Entity Type
Cooking
Font styles to use
Sans Serif
Colors
Designer to choose colors to be used in the design.
Requirements
Must have
- It must have "Beyond the Hunt" logo. It should have Scale and Plume. Scale and Plume is the type of seasoning. It must have a small place on the label for net weight. It must also have the wording "Contains: 3 Individual Cooking Bags Inside.
Nice to have
- I really like a topographical map in the background. I have attached several images with products like that. It could also be cool having the background of the bag with a tiger trout's scales. I attached some images of that too. Some other ideas I thought i have is having a picture of the bird and fish on the bag. There is an GIF attached that has a cool looking fish that did that. There is also an image of a Holvak product that did the same thing.

```html
<!DOCTYPE html>
<html lang="en">
<head>
<meta charset="utf-8">
<title>Beyond the Hunt – Scale and Plume Labels</title>
<link rel="stylesheet" href="https://fonts.googleapis.com/css2?family=Oswald:wght@400;500;600&family=Cabin+Condensed:wght@500&display=swap">
<style>
  :root {
    --page-bg: #ffffff;
    --label-bg: #141414;
    --grid-line: rgba(255, 255, 255, 0.07);
    --text-light: #f2f2f2;
    --accent-lime: #8fe32a;
    --accent-teal: #3fd3a0;
    --accent-white: #e8e8e8;
    --accent-orange: #ff5a1a;
  }
  * { box-sizing: border-box; margin: 0; padding: 0; }
  html, body {
    width: 1200px;
    height: 675px;
    overflow: hidden;
    background: var(--page-bg);
  }
  .label-range {
    width: 1200px;
    height: 675px;
    display: flex;
    align-items: center;
    justify-content: center;
    gap: 30px;
  }
  .label {
    --accent: var(--accent-white);
    width: 250px;
    height: 335px;
    border: 5px solid var(--accent);
    border-radius: 12px;
    background-color: var(--label-bg);
    background-image:
      repeating-linear-gradient(0deg, var(--grid-line) 0 1px, transparent 1px 30px),
      repeating-linear-gradient(90deg, var(--grid-line) 0 1px, transparent 1px 30px);
    display: flex;
    flex-direction: column;
    align-items: center;
    padding: 48px 18px 20px;
    color: var(--text-light);
    text-align: center;
  }
  .label--lime { --accent: var(--accent-lime); }
  .label--teal { --accent: var(--accent-teal); }
  .label--white { --accent: var(--accent-white); }
  .label--orange { --accent: var(--accent-orange); }

  .brand {
    display: flex;
    align-items: center;
    gap: 8px;
    font-family: "Oswald", sans-serif;
    font-weight: 600;
    font-size: 25px;
    letter-spacing: 0.5px;
    color: var(--text-light);
    text-transform: uppercase;
  }
  .brand__mark {
    width: 12px;
    height: 12px;
    background: var(--text-light);
  }
  .product-name {
    margin-top: 30px;
    font-family: "Oswald", sans-serif;
    font-weight: 500;
    font-size: 25px;
    letter-spacing: 0.5px;
    text-transform: uppercase;
    color: var(--text-light);
  }
  .product-name__join { font-size: 17px; }
  .product-art {
    margin-top: 14px;
    width: 130px;
    height: 52px;
    border-radius: 26px;
    background: radial-gradient(ellipse at center, var(--accent) 0%, rgba(0,0,0,0) 75%);
    opacity: 0.85;
  }
  .contents {
    margin-top: 14px;
    font-family: "Cabin Condensed", sans-serif;
    font-weight: 500;
    font-size: 10px;
    text-transform: uppercase;
    color: var(--accent);
    letter-spacing: 0.2px;
  }
  .contents__lead { font-size: 7.5px; }
  .net-weight {
    margin-top: 10px;
    font-family: "Oswald", sans-serif;
    font-weight: 400;
    font-size: 15px;
    color: var(--accent);
  }
  .net-weight__unit { font-size: 10px; }
</style>
</head>
<body>
<main class="label-range">
  <article class="label label--lime">
    <div class="brand"><span class="brand__mark"></span>Beyond the Hunt</div>
    <h1 class="product-name">Scale <span class="product-name__join">and</span> Plume</h1>
    <div class="product-art" role="img" aria-label="Line drawing of a leaping trout and a pheasant"></div>
    <p class="contents"><span class="contents__lead">Contains:</span> 3 Individual Cooking Bags Inside</p>
    <p class="net-weight">100 <span class="net-weight__unit">G</span></p>
  </article>
  <article class="label label--teal">
    <div class="brand"><span class="brand__mark"></span>Beyond the Hunt</div>
    <h1 class="product-name">Scale <span class="product-name__join">and</span> Plume</h1>
    <div class="product-art" role="img" aria-label="Line drawing of a leaping trout and a pheasant"></div>
    <p class="contents"><span class="contents__lead">Contains:</span> 3 Individual Cooking Bags Inside</p>
    <p class="net-weight">100 <span class="net-weight__unit">G</span></p>
  </article>
  <article class="label label--white">
    <div class="brand"><span class="brand__mark"></span>Beyond the Hunt</div>
    <h1 class="product-name">Scale <span class="product-name__join">and</span> Plume</h1>
    <div class="product-art" role="img" aria-label="Line drawing of a leaping trout and a pheasant"></div>
    <p class="contents"><span class="contents__lead">Contains:</span> 3 Individual Cooking Bags Inside</p>
    <p class="net-weight">100 <span class="net-weight__unit">G</span></p>
  </article>
  <article class="label label--orange">
    <div class="brand"><span class="brand__mark"></span>Beyond the Hunt</div>
    <h1 class="product-name">Scale <span class="product-name__join">and</span> Plume</h1>
    <div class="product-art" role="img" aria-label="Line drawing of a leaping trout and a pheasant"></div>
    <p class="contents"><span class="contents__lead">Contains:</span> 3 Individual Cooking Bags Inside</p>
    <p class="net-weight">100 <span class="net-weight__unit">G</span></p>
  </article>
</main>
</body>
</html>
```